Swimming Pool Supply Company Business Cards

We need business cards designed for company. These need to be easy to edit so that we can fill in names, titles, and contact info for each person who works here.

Dalton R. Pembry
Manager of Legal & Finance
J.L. Pembry, Incorporated

4837 Grelwood Avenue
Marlow Crossing, PA 19054

E. dalton@jlpembry.com
M. (215) 555-7193
O. (215) 555-4620

Contact Information for Business Card

Looking to upgrade current business cards with graphic that can be edited. Looking for fresh ideas for an age old industry.

Font styles to use
Serif
Sans Serif

Colors

Designer to choose colors to be used in the design.

Requirements
Must have
• Professional, fresh, unique but professional

```html
<!DOCTYPE html>
<html lang="en">
<head>
<meta charset="utf-8">
<title>J.L. Pembry, Incorporated – Business Cards</title>
<link rel="stylesheet" href="https://fonts.googleapis.com/css2?family=Fira+Sans:wght@400;600;700&display=swap">
<style>
  :root {
    --backdrop: #2b2d30;
    --brand-blue: #1f63b8;
    --brand-blue-deep: #1652a0;
    --ink: #2a2a2a;
    --paper: #ffffff;
    --card-w: 540px;
    --card-h: 309px;
  }
  * { box-sizing: border-box; margin: 0; padding: 0; }
  html, body {
    width: 1200px; height: 900px; overflow: hidden;
    background: var(--backdrop);
    font-family: "Fira Sans", Arial, sans-serif;
  }
  .card-sheet {
    width: 1200px; height: 900px;
    display: flex; align-items: center; justify-content: center; gap: 40px;
  }
  .card {
    position: relative;
    width: var(--card-w); height: var(--card-h);
    border-radius: 22px; overflow: hidden;
    box-shadow: 0 10px 30px rgba(0,0,0,.45);
  }

  /* Front */
  .card--front { background: var(--paper); color: var(--ink); }
  .person { position: absolute; left: 34px; top: 36px; }
  .person__name { color: var(--brand-blue); font-weight: 700; font-size: 22px; }
  .person__title { font-size: 15px; margin-top: 3px; }
  .contact-list { position: absolute; left: 34px; top: 122px; list-style: none; font-size: 15.5px; line-height: 24px; }
  .contact-list li { display: flex; align-items: center; gap: 9px; }
  .contact-list svg { width: 13px; height: 13px; flex: none; fill: none; stroke: var(--brand-blue); stroke-width: 1.6; }
  .contact-list .icon-solid { fill: var(--brand-blue); stroke: none; }

  .brand { position: absolute; right: 34px; top: 40px; text-align: left; }
  .brand__name { color: var(--brand-blue); font-weight: 700; font-size: 58px; line-height: 1; letter-spacing: 1px; }
  .brand__tagline { color: var(--brand-blue-deep); font-weight: 600; font-size: 10.5px; text-transform: uppercase; margin-top: 4px; letter-spacing: .2px; }

  .divider { position: absolute; left: 238px; right: 0; top: 186px; height: 2px; background: var(--brand-blue); }
  .company { position: absolute; left: 262px; top: 206px; font-size: 16px; line-height: 21px; }
  .company__name { color: var(--brand-blue); font-weight: 700; font-size: 17px; }

  /* Back */
  .card--back { color: var(--paper); }
  .water-texture {
    position: absolute; inset: 0;
    background: linear-gradient(160deg, #2a76d2 0%, #1f63b8 55%, #17529e 100%);
  }
  .back-brand { position: absolute; inset: 0; display: flex; flex-direction: column; align-items: center; justify-content: center; }
  .back-brand__name { font-weight: 700; font-size: 96px; line-height: 1; letter-spacing: 2px; }
  .back-brand__tagline { font-size: 16px; margin-top: 10px; }
</style>
</head>
<body>
<main class="card-sheet">
  <section class="card card--front" aria-label="Business card front">
    <div class="person">
      <p class="person__name">Dalton R. Pembry</p>
      <p class="person__title">Manager of Legal &amp; Finance</p>
    </div>
    <ul class="contact-list">
      <li><svg viewBox="0 0 14 14"><rect x="3" y="1" width="8" height="12" rx="1.5"/></svg>(215) 555-7193</li>
      <li><svg viewBox="0 0 14 14" class="icon-solid"><path d="M2 5c0-2 2-3 5-3s5 1 5 3v1H9V5H5v1H2z M3 7h8l1 5H2z"/></svg>(215) 555-4620</li>
      <li><svg viewBox="0 0 14 14" class="icon-solid"><path d="M1 3h12v1L7 8 1 4z M1 5.5l6 4 6-4V11H1z"/></svg>dalton@jlpembry.com</li>
    </ul>

    <div class="brand">
      <p class="brand__name">PEMBRY</p>
      <p class="brand__tagline">Swimming Pools, Supplies, and Accessories</p>
    </div>

    <div class="divider"></div>
    <address class="company" style="font-style:normal">
      <p class="company__name">J.L. Pembry, Incorporated</p>
      <p>4837 Grelwood Avenue</p>
      <p>Marlow Crossing, PA 19054</p>
    </address>
  </section>

  <section class="card card--back" aria-label="Business card back">
    <div class="water-texture" role="img" aria-label="Blue rippled water pattern"></div>
    <div class="back-brand">
      <p class="back-brand__name">PEMBRY</p>
      <p class="back-brand__tagline">Big Enough To Serve You, Small Enough To Care</p>
    </div>
  </section>
</main>
</body>
</html>
```